Ridgeline Outfitters Business Cards

Recently had a logo done with Artfolio and now looking for a business card to go along with it.

Target Market(s)

Ridgeline Outfitters is a weapons dealer. My market will be primarily men, hunting, shooting type.

Industry/Entity Type

Business

Contact Information for Business Card

I selected double sided, but this is not required, single or double is going to be fine. I picture the logo on one side, or perhaps just the circle which contains "RO" with the remaining info on the other side.

Font styles to use
Sans Serif

Requirements
Must have
• My name: Milo Brandt
• Title: Owner
• tel: 612-555-0187
• web: www.ridgelineoutfittersmn.example
Nice to have
• I like the concept of a black business card. I would like to keep the colors monotone, black, grey, white or red. Red is acceptable because it is in the logo. I have also seen cards that are matte black with shiny black as well, perhaps for the logo (or circle RO) part of the logo.
• I will upload a couple of the logos for use, and also an example I just found of the black on black. and some others that have a nice contrast.
Should not have
• lots of colors are not wanted.

```html
<!DOCTYPE html>
<html lang="en">
<head>
<meta charset="utf-8">
<title>Ridgeline Outfitters Business Card</title>
<link rel="stylesheet" href="https://fonts.googleapis.com/css2?family=Open+Sans:wght@300;400;600&display=swap">
<style>
  :root {
    --bg: #e4e1dc;
    --card: #efece8;
    --charcoal: #29262d;
    --red: #d23636;
    --ink: #1c1b1f;
  }
  html, body {
    margin: 0;
    width: 1200px;
    height: 799px;
    overflow: hidden;
    background: var(--bg);
    font-family: "Open Sans", sans-serif;
  }
  .business-card {
    position: absolute;
    left: 180px;
    top: 160px;
    width: 840px;
    height: 480px;
    background: var(--card);
    box-shadow: 0 6px 24px rgba(0,0,0,0.15);
    overflow: hidden;
  }
  .card-bands {
    position: absolute;
    inset: 0;
  }
  .brand-lockup {
    position: absolute;
    right: 60px;
    top: 58px;
    display: flex;
    align-items: center;
    gap: 14px;
  }
  .brand-mark {
    width: 40px;
    height: 40px;
    border-radius: 50%;
    background: var(--red);
  }
  .brand-name {
    color: var(--red);
    font-weight: 600;
    font-size: 24px;
    letter-spacing: 1px;
    text-transform: uppercase;
  }
  .holder-name {
    position: absolute;
    left: 64px;
    top: 168px;
    margin: 0;
    font-weight: 300;
    font-size: 50px;
    color: var(--ink);
    letter-spacing: 0.5px;
  }
  .holder-details {
    position: absolute;
    left: 66px;
    top: 240px;
    margin: 0;
    padding: 0;
    list-style: none;
    font-size: 15px;
    line-height: 22px;
    color: var(--ink);
  }
  .website {
    position: absolute;
    right: 50px;
    bottom: 40px;
    font-size: 15px;
    font-weight: 600;
    color: var(--ink);
  }
</style>
</head>
<body>
  <div class="business-card">
    <svg class="card-bands" width="840" height="480" viewBox="0 0 840 480" aria-hidden="true">
      <rect x="0" y="0" width="840" height="130" fill="var(--charcoal)"/>
      <rect x="0" y="130" width="840" height="8" fill="var(--red)"/>
      <polygon points="598,138 840,138 840,174 610,174" fill="var(--red)"/>
      <polygon points="590,130 604,130 616,162 604,162" fill="var(--charcoal)"/>
    </svg>
    <div class="brand-lockup">
      <span class="brand-mark"></span>
      <span class="brand-name">Ridgeline Outfitters</span>
    </div>
    <h1 class="holder-name">Milo Brandt</h1>
    <ul class="holder-details">
      <li>// Owner</li>
      <li>// 612-555-0187</li>
    </ul>
    <div class="website">www.ridgelineoutfittersmn.example</div>
  </div>
</body>
</html>
```